Label or packaging Design for Hair Care Line

Dear Designer,
We are Corvella, a brand known for our premium hairstyling tools, and we are excited to expand into hair care. We are currently looking for a talented designer to create the label designs for our entire luxury hair care line.
This project is crucial in establishing our visual identity in the hair care market, and we aim to position ourselves alongside premium brands such as LTP, Dorvane Hair Atelier, and Pelmi.
Project Scope
We need a cohesive label design for our hair care line, which includes:
5 products (e.g., shampoo, conditioner, hair oil, styling cream, and a hair mask).
The designs should include:
Front label: Highlighting the product name, key features, and branding.
Our goal is to achieve a design that communicates premium luxury with a touch of professionalism. Below are the specific guidelines to help you align with our vision:
Style and Inspiration
Think of brands like LTP, Dorvane Hair Atelier, and Pelmi.
Luxury and Minimalism: Clean lines, sophisticated typography, and an elegant color palette.
Subtle femininity: premium finishes like metallic accents (gold, silver, or rose gold).
Brand Personality
Premium: Reflecting high quality and exclusivity.
Modern & Professional: Appealing to a refined, professional audience but also suitable for lifestyle-oriented customers.
Warm & Empowering: A brand that celebrates confidence and individuality.
Color Palette
Neutral tones like black, white, accented with metallics (gold or silver) for a luxurious feel.
Colors that feel timeless and elegant rather than trendy or overly bright.
Typography
Use clean, modern fonts (preferably sans-serif or serif for a refined look).
Clear and legible for all product details while maintaining a high-end aesthetic.
Materials and Finishes
Packaging Shape
The label designs should suit a variety of bottle and jar shapes (e.g., cylindrical, flat, or rounded).
Keep scalability in mind so the identity remains consistent across different products.
Deliverables
To understand the aesthetic we are aiming for, here are some brands to use as inspiration:
LTP: For its minimalistic and modern approach.
Dorvane Hair Atelier: For its combination of luxury and professional appeal.
Pelmi: For its soft femininity and lifestyle branding.
we would like to see your designs applied to a variety of packaging types to get an overall impression of how the brand identity works across different product formats. This includes:
A squeeze bottle (e.g., for styling creams or conditioners).
A glass bottle with a dropper (e.g., for a luxurious hair oil).
A shampoo/conditioner bottle (standard pump or flip-top cap).
A spray bottle (e.g., for leave-in treatments or heat protectors).
By creating designs for these different packaging types, we can better evaluate how cohesive and versatile the brand identity will be across the entire product line.

Updates
As you may have noticed from the designs, they don’t quite align with our briefing. The look needs to be clean and professional, similar to Dorvane, LTP, and the other examples we provided. Please address this, and we’ll check it!

Target Market(s)
europe and us
Font styles to use
Other font styles liked:
- century gothic

Look and feel
Each slider illustrates characteristics of the customer's brand and the style your logo design should communicate.

```html
<!DOCTYPE html>
<html lang="en">
<head>
<meta charset="utf-8">
<title>Corvella Hair Shampoo – Label Options</title>
<link rel="stylesheet" href="https://fonts.googleapis.com/css2?family=Bodoni+Moda:opsz,wght@6..96,600&family=Montserrat:wght@400;500&display=swap">
<style>
  :root {
    --paper: #ffffff;
    --ink: #0b0b0b;
    --ring-line: #111111;
    --gold-peach: #f8bd94;
    --gold-cream: #fbe7b6;
    --gold-pale: #fcf6c6;
  }
  * { margin: 0; padding: 0; box-sizing: border-box; }
  html, body {
    width: 1200px;
    height: 848px;
    overflow: hidden;
    background: var(--paper);
  }
  .sheet {
    position: relative;
    width: 1200px;
    height: 848px;
  }
  .label {
    position: absolute;
    top: 217px;
    width: 414px;
    height: 414px;
  }
  .label--outline { left: 168px; }
  .label--gilded  { left: 617px; }
  .label__ring {
    position: absolute;
    inset: 0;
    width: 100%;
    height: 100%;
  }
  .label__content {
    position: absolute;
    inset: 0;
    display: flex;
    flex-direction: column;
    align-items: center;
    color: var(--ink);
    text-align: center;
  }
  .label__brand {
    margin-top: 118px;
    font-family: "Montserrat", sans-serif;
    font-weight: 400;
    font-size: 66px;
    line-height: 1;
    letter-spacing: 1px;
  }
  .label__product {
    margin-top: 26px;
    font-family: "Bodoni Moda", serif;
    font-weight: 600;
    font-size: 34px;
    line-height: 1;
    letter-spacing: 4px;
  }
  .label__claim {
    margin-top: 12px;
    font-family: "Montserrat", sans-serif;
    font-weight: 500;
    font-size: 10.5px;
    line-height: 13px;
    letter-spacing: 1.1px;
    text-transform: uppercase;
  }
</style>
</head>
<body>
<main class="sheet">

  <section class="label label--outline">
    <svg class="label__ring" viewBox="0 0 414 414" aria-hidden="true">
      <circle cx="207" cy="207" r="206" fill="none" stroke="var(--ring-line)" stroke-width="1"/>
    </svg>
    <div class="label__content">
      <p class="label__brand">Corvella</p>
      <h2 class="label__product">HAIR SHAMPOO</h2>
      <p class="label__claim">Leaves hair smooth, rejuvenated and<br>restored without looking greasy</p>
    </div>
  </section>

  <section class="label label--gilded">
    <svg class="label__ring" viewBox="0 0 414 414" aria-hidden="true">
      <defs>
        <linearGradient id="gilded-ring" x1="0" y1="0" x2="1" y2="0">
          <stop offset="0" stop-color="var(--gold-peach)"/>
          <stop offset="0.3" stop-color="var(--gold-cream)"/>
          <stop offset="0.55" stop-color="var(--gold-pale)"/>
          <stop offset="1" stop-color="var(--gold-pale)"/>
        </linearGradient>
      </defs>
      <circle cx="207" cy="207" r="197" fill="none" stroke="url(#gilded-ring)" stroke-width="19"/>
    </svg>
    <div class="label__content">
      <p class="label__brand">Corvella</p>
      <h2 class="label__product">HAIR SHAMPOO</h2>
      <p class="label__claim">Leaves hair smooth, rejuvenated and<br>restored without looking greasy</p>
    </div>
  </section>

</main>
</body>
</html>
```